landscaping core flute signs

I need core flutes created with business name and a few extra dot points for putting on fences for job sites 120cm x 120cm approx.
I want our old ones information with the new L logo and colour palette

```html
<!DOCTYPE html>
<html lang="en">
<head>
<meta charset="utf-8">
<title>Terrace Field – Site Sign</title>
<link href="https://fonts.googleapis.com/css2?family=Roboto:wght@400;500;700&display=swap" rel="stylesheet">
<style>
  :root {
    --leaf: #5f8b56;
    --ink: #000000;
    --paper: #ffffff;
  }
  * { margin: 0; padding: 0; box-sizing: border-box; }
  html, body {
    width: 1200px;
    height: 1200px;
    overflow: hidden;
    background: var(--paper);
    font-family: "Roboto", Arial, sans-serif;
  }
  .sign {
    position: relative;
    width: 1200px;
    height: 1200px;
    background: var(--paper);
  }
  .brand-mark {
    position: absolute;
    left: 469px;
    top: 60px;
    width: 262px;
    height: 262px;
    border-radius: 50%;
    background: var(--leaf);
  }
  .brand-name {
    position: absolute;
    left: 0;
    top: 348px;
    width: 1200px;
    text-align: center;
    font-weight: 500;
    font-size: 74px;
    letter-spacing: 4px;
    color: var(--ink);
    line-height: 1;
  }
  .tagline {
    position: absolute;
    left: 0;
    top: 478px;
    width: 1200px;
    text-align: center;
    font-weight: 400;
    font-size: 19px;
    letter-spacing: 6px;
    text-transform: uppercase;
    color: var(--leaf);
  }
  .services {
    position: absolute;
    left: 307px;
    top: 586px;
    list-style: none;
  }
  .services li {
    display: flex;
    align-items: center;
    height: 86.5px;
    font-weight: 500;
    font-size: 49px;
    color: var(--ink);
  }
  .services li::before {
    content: "";
    width: 60px;
    height: 60px;
    border-radius: 50%;
    background: var(--leaf);
    margin-right: 50px;
    flex: none;
  }
  .phone-band {
    position: absolute;
    left: 0;
    top: 878px;
    width: 1200px;
    height: 182px;
    background: var(--leaf);
    display: flex;
    align-items: center;
    justify-content: center;
  }
  .phone {
    font-weight: 700;
    font-size: 176px;
    color: var(--paper);
    line-height: 1;
    letter-spacing: 1px;
  }
  .email {
    position: absolute;
    left: 0;
    top: 1070px;
    width: 1200px;
    text-align: center;
    font-weight: 400;
    font-size: 62px;
    color: var(--leaf);
    line-height: 1;
  }
</style>
</head>
<body>
  <main class="sign">
    <div class="brand-mark" aria-hidden="true"></div>
    <h1 class="brand-name">TERRACE FIELD</h1>
    <p class="tagline">Structural Landscaping</p>
    <ul class="services">
      <li>Paving &amp; Concreting</li>
      <li>Fencing &amp; Retaining</li>
      <li>Design &amp; Construct</li>
    </ul>
    <div class="phone-band">
      <p class="phone">0400 218 695</p>
    </div>
    <p class="email">sam@terracefield.com</p>
  </main>
</body>
</html>
```